依頼詳細
・色は1~2色
・慶事で使用できるような華やかなデザインを希望します
・弊社ロゴ画像を添付しております。どれを使用していただいても構いません。(ロゴ使用に関しては必須ではございません)
記載項目
サイズ…約200㎜(縦)×約120㎜(横)×約30㎜(高さ)
(開き方は画像をご参照頂ければと思います。)
希望イメージ
シンプル 複雑
単色 カラフル
暗い 明るい
日常 高級
遊び心 厳粛
未来的 伝統的
女性的 男性的
希望する色
納品ファイル
• イラストレーター形式 (.ai)
補足説明
向きは縦長でお願い致します。
■ 選んだ理由

華やかすぎない、上品なデザインをご提案頂いた点。
今まで弊社に無かったスタイルでありながら、弊社の他の商品ラインナップと比較した時に違和感なくラインナップに入るデザインであった点が良かったです。

■ 提案者全員のお礼・コメント

たくさんのご提案を頂き、本当にありがとうございます。
私どもでは思いもよらなかった素敵なデザインばかりで、大変感激しております。

ありがとうございました。

```html
<!DOCTYPE html>
<html lang="ja">
<head>
<meta charset="utf-8">
<title>Koto Hana – Gift Box Lid</title>
<link rel="stylesheet" href="https://fonts.googleapis.com/css2?family=Montserrat:wght@300&display=swap">
<style>
  :root {
    --paper: #ffffff;
    --frame: #d6d6d6;
    --vermilion: #e0434f;
    --blush: #f7dfe1;
    --ink-grey: #8c8c8c;
  }
  html, body {
    margin: 0;
    padding: 0;
    width: 762px;
    height: 1200px;
    overflow: hidden;
    background: var(--paper);
  }
  .box-lid {
    position: relative;
    width: 762px;
    height: 1200px;
  }
  .box-lid__art {
    position: absolute;
    inset: 0;
    display: block;
  }
  .lid-frame { fill: none; stroke: var(--frame); stroke-width: 2; }
  .diamond--red { fill: var(--vermilion); }
  .diamond--pattern { fill: var(--blush); }
  .brand-dot { fill: var(--vermilion); }
  .brand-name {
    position: absolute;
    left: 0;
    width: 762px;
    top: 666px;
    margin: 0;
    text-align: center;
    font-family: "Montserrat", sans-serif;
    font-weight: 300;
    font-size: 22px;
    line-height: 28px;
    letter-spacing: 0.3em;
    text-indent: 0.3em;
    color: var(--ink-grey);
  }
</style>
</head>
<body>
  <main class="box-lid">
    <svg class="box-lid__art" width="762" height="1200" viewBox="0 0 762 1200" xmlns="http://www.w3.org/2000/svg">
      <defs>
        <clipPath id="lid-face">
          <rect x="46" y="118" width="670" height="964"/>
        </clipPath>
      </defs>

      <rect class="lid-frame" x="8" y="8" width="746" height="1184"/>

      <g clip-path="url(#lid-face)">
        <polygon class="diamond--pattern" role="img"
                 aria-label="Shippo interlocking-circle pattern in red line on white"
                 points="-101,359 140,600 -101,841 -342,600"/>
        <polygon class="diamond--pattern" role="img"
                 aria-label="Asanoha hemp-leaf pattern in red line on white"
                 points="863,359 1104,600 863,841 622,600"/>

        <polygon class="diamond--red"
                 points="140,118 381,359 140,600 -101,359"/>
        <polygon class="diamond--red" role="img"
                 aria-label="Red field with a large white mizuhiki knot"
                 points="622,118 863,359 622,600 381,359"/>
        <polygon class="diamond--red" role="img"
                 aria-label="Red field with white stylised pine trees on rolling hills"
                 points="140,600 381,841 140,1082 -101,841"/>
        <polygon class="diamond--red"
                 points="622,600 863,841 622,1082 381,841"/>
      </g>

      <circle class="brand-dot" cx="381" cy="552" r="80"/>
    </svg>

    <p class="brand-name">KOTO HANA</p>
  </main>
</body>
</html>
```